Web design for boutique law firm

Web design for law firm; practice areas include:
-international intellectual property counseling
-general corporate (contract negotiation, licensing, distribution agreements
-see my *very* outdated website at www.pvtlegalhouse.com: here is some of the home page content:

"PVT Law Group enjoys providing proactive, business-minded, efficient legal solutions for individuals and companies that benefit from major law firm experience at reasonable rates.

Some areas of emphasis include:

Counseling individuals and companies with respect to clearing, selecting, securing, managing, commercializing, and protecting intellectual property assets around the world. This includes traditional global brand management, marketing, advertising, and enforcement work as well as litigation.
PVT Law Group also provides general counseling services for individuals and businesses, from start-up advice to sophisticated business transactions strategy, agreement negotiating, dispute resolution, and litigation.
Before founding PVT Law Group in 2008, Curtis L. Abernathy led the Trademark, Copyright, & Brand Management Group for Falkner & Ingleby's Seattle office. Curtis was also a senior associate at Silicon Valley based Hartwell, Bexley, Oduya, & Penrose."

Target Market(s)

Clients/potential clients needing tier one, international intellectual property advice with "mega" law firm experience for much less than what we were/would be charging at the "mega firms".

Industry/Entity Type

Legal

Number of Pages Required

4 page

Font styles to use
Serif
Sans Serif

Colors

Designer to choose colors to be used in the design.

Requirements
Must have
• +Improvement over everything on current site at www.pvtlegalhouse.com.
• +Pictures/bios for me and my team (four of us right now).
• +Easy to update and add/remove content.
• +Must be superior in design (look, feel, ease of use, classy and elegant, but hip, reflects international practice).
• +i have logos and color schemes (see current website) but will consider improvements.
Nice to have
• Let me know your thoughts.
Should not have
• No cheese; no overt sales pitches or marketing (since law firm).

```html
<!DOCTYPE html>
<html lang="en">
<head>
<meta charset="utf-8">
<title>PVT Law Group PLLC</title>
<link rel="stylesheet" href="https://fonts.googleapis.com/css2?family=Quattrocento:wght@400;700&family=Open+Sans:wght@400;600;700&display=swap">
<style>
:root{
  --orange:#d4590f;
  --black:#050505;
  --ink:#2b2b2b;
  --muted:#6a6a6a;
  --light:#f3f4f6;
  --card:#f4f4f5;
  --field:#b5b5b5;
  --line:#d9d9d9;
  --white:#ffffff;
  --serif:'Quattrocento', Georgia, serif;
  --sans:'Open Sans', Arial, sans-serif;
}
*{box-sizing:border-box;margin:0;padding:0}
html,body{width:1200px;height:3629px;overflow:hidden}
body{font-family:var(--sans);color:var(--ink);background:var(--white);position:relative}
section,header,footer{position:relative;width:1200px}
.section-title{font-family:var(--serif);font-weight:700;font-size:25px;letter-spacing:1px;text-align:center;text-transform:uppercase}
.title-rule{width:52px;height:3px;background:var(--orange);margin:14px auto 0}
.arrow{position:absolute;width:50px;height:46px;display:flex;align-items:center;justify-content:center}
.arrow.prev{left:0;background:#e2e2e2}
.arrow.next{right:0;background:var(--orange)}
.arrow svg{width:14px;height:14px}
.btn{display:inline-flex;align-items:center;gap:10px;background:var(--orange);color:var(--white);font-family:var(--serif);font-weight:700;font-size:14px;letter-spacing:1px;text-transform:uppercase;padding:0 18px;height:42px}
.stars{color:var(--orange);letter-spacing:2px;font-size:15px}

/* header */
.site-header{height:97px;display:flex;align-items:center;justify-content:space-between;padding:0 130px}
.brand{display:flex;align-items:center;gap:10px;font-family:var(--serif);color:var(--orange);font-size:24px;font-weight:400;letter-spacing:0.5px}
.brand-mark{width:14px;height:14px;background:var(--orange)}
.header-right{display:flex;flex-direction:column;align-items:flex-end;gap:12px}
.call{font-size:14px;color:var(--muted);display:flex;align-items:center;gap:6px}
.call strong{font-size:25px;color:var(--orange);font-weight:700}
.main-nav{display:flex;gap:32px;font-size:14px;color:var(--ink);align-items:center}
.main-nav .active{color:var(--orange)}

/* hero */
.hero{height:483px;background:linear-gradient(100deg,#3a4148 0%,#5b5c57 35%,#8a6a40 70%,#b36a1e 100%)}
.hero-photo{position:absolute;inset:0}
.hero-copy{position:absolute;left:560px;top:130px;width:480px;color:var(--white)}
.hero-copy h1{font-family:var(--serif);font-weight:700;font-size:29px;line-height:1.35;letter-spacing:1px;text-transform:uppercase}
.hero-copy p{font-size:15px;line-height:1.5;margin:14px 0 22px}

/* practice */
.practice{height:432px;padding-top:52px}
.practice-cards{position:absolute;top:132px;left:130px;display:flex;gap:40px}
.practice-card{width:205px;height:178px;background:var(--card);display:flex;flex-direction:column;align-items:center;padding-top:36px}
.practice-card.active{background:var(--orange);color:var(--white)}
.practice-card .icon{width:74px;height:74px;border-radius:50%;background:#e3e3e3;display:flex;align-items:center;justify-content:center}
.practice-card.active .icon{background:#f6e3d6}
.practice-card h3{font-family:var(--serif);font-weight:400;font-size:18px;margin-top:24px}
.practice .arrow{top:223px}

/* members */
.members{height:483px;background:var(--black);color:var(--white);padding-top:50px}
.members .lead{text-align:center;font-size:13px;line-height:1.7;margin:22px auto 0;width:560px}
.member-cards{position:absolute;top:200px;left:128px;display:flex;gap:40px}
.member-card{width:452px;height:219px;display:flex}
.member-photo{width:210px;height:100%;background:linear-gradient(160deg,#cfcfcf,#6e6e6e)}
.member-card .info{flex:1;padding:16px 20px;font-size:12.5px;line-height:1.55}
.member-card.featured .info{background:var(--orange)}
.member-card.plain .info{background:var(--white);color:var(--ink)}
.member-card h3{font-family:var(--serif);font-weight:400;font-size:21px;margin-bottom:6px;white-space:nowrap}
.member-card .areas{margin-top:14px}
.member-card.plain .areas span{color:var(--orange)}
.member-card .reviews{margin-top:14px;display:flex;gap:6px;align-items:center}
.member-card.featured .stars{color:var(--white)}
.members .arrow{top:316px}
.dots{position:absolute;top:432px;left:0;width:1200px;display:flex;justify-content:center;gap:8px}
.dots i{width:6px;height:6px;border-radius:50%;background:#555}
.dots i.on{background:var(--white)}

/* about */
.about{height:483px;padding-top:48px;text-align:center}
.about p{font-size:13px;line-height:1.7;color:var(--muted);width:800px;margin:0 auto}
.about .intro{margin-top:34px;width:720px}
.emphasis{display:inline-block;border:1px solid var(--orange);color:var(--orange);font-size:12.5px;padding:8px 20px;margin:24px 0 18px}
.about hr{border:0;border-top:1px solid var(--line);width:820px;margin:14px auto}
.about .btn{margin-top:40px;height:40px}

/* testimonials */
.testimonials{height:472px;background:var(--light);padding-top:48px}
.quote-cards{position:absolute;top:120px;left:128px;display:flex;gap:35px}
.quote{width:292px}
.quote .box{height:207px;overflow:hidden;background:var(--white);border:1px solid #dcdcdc;padding:18px 22px;font-size:12.5px;line-height:1.8;color:var(--muted)}
.quote .who{display:flex;align-items:center;gap:16px;margin-top:26px;padding-left:16px}
.avatar{width:62px;height:62px;border-radius:50%;background:linear-gradient(150deg,#d8d8d8,#8b8b8b)}
.who h4{font-weight:400;font-size:15px}
.who .rev{font-size:12px;display:flex;gap:6px;align-items:center;margin-top:4px}
.testimonials .arrow{top:210px}

/* clients */
.clients{height:165px;background:var(--black);display:flex;align-items:center;justify-content:space-between;padding:0 130px}
.client{display:flex;align-items:center;gap:10px;font-family:var(--serif);font-size:30px;color:#5d5d5d}
.client i{width:24px;height:24px;border-radius:50%;background:#5d5d5d}

/* contact */
.contact{height:690px;padding-top:50px;text-align:center}
.contact .ask{font-family:var(--serif);font-size:25px;color:#8a8a8a;margin-top:26px}
.contact .how{font-size:15px;line-height:1.7;color:var(--muted);margin-top:14px}
.contact .how b{color:var(--ink);font-weight:600}
.contact-form{position:absolute;top:230px;left:128px;width:945px}
.row{display:flex;gap:24px;margin-bottom:16px}
.field{flex:1;height:45px;background:var(--field);color:var(--white);font-size:15px;text-align:left;padding:12px 22px}
.field.comment{height:116px}
.captcha{width:266px;height:68px;border:1px solid #cfcfcf;background:#f9f9f9;display:flex;align-items:center;gap:14px;padding:0 14px;font-size:13px;box-shadow:0 1px 3px rgba(0,0,0,.1)}
.captcha .check{width:26px;height:26px;border:2px solid #c1c1c1;background:var(--white)}
.captcha .badge{margin-left:auto;width:34px;height:34px;background:#c9d3e6}
.submit{display:block;margin:22px auto 0;width:105px;height:42px;line-height:42px;background:var(--orange);color:var(--white);font-family:var(--serif);font-weight:700;font-size:13px;letter-spacing:1px}

/* footer */
.site-footer{height:324px;background:var(--black);color:var(--white)}
.footer-cols{display:flex;justify-content:center;height:180px}
.footer-col{width:313px;text-align:center;position:relative;padding-top:72px}
.footer-col+.footer-col{border-left:1px solid #2a2a2a}
.footer-col .badge{position:absolute;top:-18px;left:50%;margin-left:-30px;width:60px;height:60px;border-radius:50%;background:var(--orange);display:flex;align-items:center;justify-content:center}
.footer-col h4{font-family:var(--serif);font-size:20px;font-weight:700}
.footer-col p{font-size:14px;line-height:1.6;color:#bdbdbd;margin-top:8px}
.footer-col .phone{font-size:20px;color:#e0e0e0}
.social{display:flex;justify-content:center;gap:16px;margin-top:16px}
.social i{width:12px;height:12px;border-radius:50%;background:var(--white)}
.footer-nav{border-top:1px solid #1e1e1e;margin-top:12px;display:flex;justify-content:center;gap:46px;padding-top:24px;font-size:13px;letter-spacing:1px;color:#bdbdbd}
.footer-nav .active{color:var(--orange)}
.copyright{text-align:center;font-size:12px;color:#8a8a8a;margin-top:46px;border-top:1px solid #1e1e1e;padding-top:20px;width:1200px}
</style>
</head>
<body>

<header class="site-header">
  <div class="brand"><span class="brand-mark"></span>PVT Law Group PLLC</div>
  <div class="header-right">
    <div class="call">
      <svg width="14" height="14" viewBox="0 0 24 24"><path fill="#6a6a6a" d="M6.6 10.8a15 15 0 0 0 6.6 6.6l2.2-2.2c.3-.3.7-.4 1-.2 1.1.4 2.3.6 3.6.6.6 0 1 .4 1 1V20c0 .6-.4 1-1 1A17 17 0 0 1 3 4c0-.6.4-1 1-1h3.5c.6 0 1 .4 1 1 0 1.3.2 2.5.6 3.6.1.3 0 .7-.2 1z"/></svg>
      Call Us: <strong>206.555.0148</strong>
    </div>
    <nav class="main-nav">
      <span class="active">Home</span><span>Experience</span><span>About</span><span>Contact</span>
      <svg width="12" height="12" viewBox="0 0 24 24"><circle cx="10" cy="10" r="7" fill="none" stroke="#2b2b2b" stroke-width="3"/><path d="M15 15l7 7" stroke="#2b2b2b" stroke-width="3"/></svg>
    </nav>
  </div>
</header>

<section class="hero">
  <div class="hero-photo" role="img" aria-label="Seattle city skyline at dusk with the observation tower, toned in warm orange"></div>
  <div class="hero-copy">
    <h1>International Intellectual Property Counseling</h1>
    <p>PVT Law Group enjoys providing proactive, business-minded, efficient legal solutions for individuals and companies that benefit from major law firm experience at reasonable rates.</p>
    <span class="btn">How we can help you
      <svg width="16" height="16" viewBox="0 0 24 24"><circle cx="12" cy="12" r="10" fill="none" stroke="#fff" stroke-width="2"/><path d="M10 7l5 5-5 5" fill="none" stroke="#fff" stroke-width="2"/></svg>
    </span>
  </div>
</section>

<section class="practice">
  <h2 class="section-title">Areas of Practice</h2>
  <div class="title-rule"></div>
  <div class="arrow prev"><svg viewBox="0 0 14 14"><path d="M9 2L4 7l5 5" fill="none" stroke="#fff" stroke-width="2"/></svg></div>
  <div class="practice-cards">
    <div class="practice-card">
      <div class="icon"><svg width="34" height="34" viewBox="0 0 34 34"><circle cx="17" cy="10" r="5" fill="#2b2b2b"/><path d="M6 28c1-7 6-10 11-10s10 3 11 10z" fill="#2b2b2b"/></svg></div>
      <h3>Brand Management</h3>
    </div>
    <div class="practice-card active">
      <div class="icon"><svg width="34" height="34" viewBox="0 0 34 34"><rect x="8" y="8" width="14" height="7" transform="rotate(-35 15 11)" fill="#d4590f"/><path d="M17 15l10 10" stroke="#d4590f" stroke-width="3"/><rect x="5" y="26" width="14" height="3" fill="#d4590f"/></svg></div>
      <h3>Brand Enforcement</h3>
    </div>
    <div class="practice-card">
      <div class="icon"><svg width="34" height="34" viewBox="0 0 34 34"><circle cx="17" cy="17" r="11" fill="none" stroke="#2b2b2b" stroke-width="3"/><path d="M9 25L25 9" stroke="#2b2b2b" stroke-width="3"/></svg></div>
      <h3>Counterfeiting</h3>
    </div>
    <div class="practice-card">
      <div class="icon"><svg width="34" height="34" viewBox="0 0 34 34"><rect x="8" y="6" width="18" height="22" fill="none" stroke="#2b2b2b" stroke-width="2.5"/><path d="M12 12h10M12 17h10M12 22h6" stroke="#2b2b2b" stroke-width="2"/></svg></div>
      <h3>Litigation</h3>
    </div>
  </div>
  <div class="arrow next"><svg viewBox="0 0 14 14"><path d="M5 2l5 5-5 5" fill="none" stroke="#fff" stroke-width="2"/></svg></div>
</section>

<section class="members">
  <h2 class="section-title">Members Profile</h2>
  <p class="lead">The experienced members at PVT Law Group work with our clients to provide advice and results. To learn more about our members, review the profiles below.</p>
  <div class="arrow prev" style="background:#3a3a3a"><svg viewBox="0 0 14 14"><path d="M9 2L4 7l5 5" fill="none" stroke="#fff" stroke-width="2"/></svg></div>
  <div class="member-cards">
    <article class="member-card featured">
      <div class="member-photo" role="img" aria-label="Black and white portrait of Curtis L. Abernathy"></div>
      <div class="info">
        <h3>Curtis L. Abernathy</h3>
        <p>Curtis has over 30 years of experience in this fiield.</p>
        <p class="areas">Practice Areas: Individual and corporate identities, brands, and reputations</p>
        <div class="reviews">Reviews: <span class="stars">★★★★★</span></div>
      </div>
    </article>
    <article class="member-card plain">
      <div class="member-photo" role="img" aria-label="Portrait of a firm member in a dark suit" style="background:linear-gradient(160deg,#c9c4bd,#4a4f58)"></div>
      <div class="info">
        <h3>Member's Name</h3>
        <p>Curtis has over 30 years of experience in this fiield.</p>
        <p class="areas">Practice Areas: <span>Individual and corporate identities, brands, and reputations</span></p>
        <div class="reviews">Reviews: <span class="stars">★★★★★</span></div>
      </div>
    </article>
  </div>
  <div class="arrow next"><svg viewBox="0 0 14 14"><path d="M5 2l5 5-5 5" fill="none" stroke="#fff" stroke-width="2"/></svg></div>
  <div class="dots"><i class="on"></i><i></i></div>
</section>

<section class="about">
  <h2 class="section-title">About the Group</h2>
  <div class="title-rule"></div>
  <p class="intro">PVT Law Group enjoys providing proactive, business-minded, efficient legal solutions for individuals and companies that benefit from major law firm experience at reasonable rates.</p>
  <span class="emphasis">Some areas of emphasis include:</span>
  <p>Counseling individuals and companies with respect to clearing, selecting, securing, managing, commercializing, and protecting intellectual property assets around the world. This includes traditional global brand management, marketing, advertising, and enforcement work as well as litigation.</p>
  <hr>
  <p>PVT Law Group also provides general counseling services for individuals and businesses, from start-up advice to sophisticated business transactions strategy, agreement negotiating, dispute resolution, and litigation.</p>
  <span class="btn">Read more
    <svg width="16" height="16" viewBox="0 0 24 24"><circle cx="12" cy="12" r="10" fill="none" stroke="#fff" stroke-width="2"/><path d="M10 7l5 5-5 5" fill="none" stroke="#fff" stroke-width="2"/></svg>
  </span>
</section>

<section class="testimonials">
  <h2 class="section-title">What Our Clients Say</h2>
  <div class="title-rule"></div>
  <div class="arrow prev"><svg viewBox="0 0 14 14"><path d="M9 2L4 7l5 5" fill="none" stroke="#fff" stroke-width="2"/></svg></div>
  <div class="quote-cards">
    <div class="quote">
      <div class="box">Lorem ipsum dolor sit amet, consectetur adipisicing elit, sed do eiusmod tempor incididunt ut labore et dolore magna aliqua. Ut enim ad minim veniam, quis nostrud exercitation ullamco laboris nisi ut aliquip ex ea commodo consequat. Duis aute irure dolor in reprehenderit...</div>
      <div class="who"><div class="avatar" role="img" aria-label="Client portrait"></div><div><h4>Owen Bracey</h4><div class="rev">Reviews: <span class="stars">★★★★★</span></div></div></div>
    </div>
    <div class="quote">
      <div class="box">Lorem ipsum dolor sit amet, consectetur adipisicing elit, sed do eiusmod tempor incididunt ut labore et dolore magna aliqua. Ut enim ad minim veniam, quis nostrud exercitation ullamco laboris nisi ut aliquip ex ea commodo consequat. Duis aute irure dolor in reprehenderit...</div>
      <div class="who"><div class="avatar" role="img" aria-label="Client portrait"></div><div><h4>Lena Marsh</h4><div class="rev">Reviews: <span class="stars">★★★★★</span></div></div></div>
    </div>
    <div class="quote">
      <div class="box">Lorem ipsum dolor sit amet, consectetur adipisicing elit, sed do eiusmod tempor incididunt ut labore et dolore magna aliqua. Ut enim ad minim veniam, quis nostrud exercitation ullamco laboris nisi ut aliquip ex ea commodo consequat. Duis aute irure dolor in reprehenderit...</div>
      <div class="who"><div class="avatar" role="img" aria-label="Client portrait"></div><div><h4>Theo Vance</h4><div class="rev">Reviews: <span class="stars">★★★★★</span></div></div></div>
    </div>
  </div>
  <div class="arrow next"><svg viewBox="0 0 14 14"><path d="M5 2l5 5-5 5" fill="none" stroke="#fff" stroke-width="2"/></svg></div>
</section>

<section class="clients">
  <div class="client"><i></i>Northvale</div>
  <div class="client">Ashgrove Capital</div>
  <div class="client">Orchard</div>
  <div class="client">Corelith</div>
  <div class="client"><i></i>Travanta</div>
</section>

<section class="contact">
  <h2 class="section-title">Contact Info</h2>
  <p class="ask">Do you have question? We can help!</p>
  <p class="how">To speak to our member, please call us at <b>206.555.0148</b> or e-mail us at <b>contact@pvtlawgroup.com</b>.<br>You can also contact us by filling out the following form:</p>
  <form class="contact-form">
    <div class="row"><div class="field">First Name</div><div class="field">Last Name</div></div>
    <div class="row"><div class="field">Email Address</div><div class="field">Phone Number</div></div>
    <div class="row"><div class="field comment">Comment</div></div>
    <div class="captcha"><span class="check"></span>I'm not a robot<span class="badge"></span></div>
    <span class="submit">SUBMIT</span>
  </form>
</section>

<footer class="site-footer">
  <div class="footer-cols">
    <div class="footer-col">
      <span class="badge"><svg width="24" height="24" viewBox="0 0 24 24"><path d="M12 2a7 7 0 0 0-7 7c0 5 7 13 7 13s7-8 7-13a7 7 0 0 0-7-7z" fill="none" stroke="#fff" stroke-width="2"/><circle cx="12" cy="9" r="2.5" fill="#fff"/></svg></span>
      <h4>Address</h4>
      <p>402 W. Harbor Ave. Suite C, Seattle<br>WA. 98119</p>
    </div>
    <div class="footer-col">
      <span class="badge"><svg width="24" height="24" viewBox="0 0 24 24"><path fill="#fff" d="M6.6 10.8a15 15 0 0 0 6.6 6.6l2.2-2.2c.3-.3.7-.4 1-.2 1.1.4 2.3.6 3.6.6.6 0 1 .4 1 1V20c0 .6-.4 1-1 1A17 17 0 0 1 3 4c0-.6.4-1 1-1h3.5c.6 0 1 .4 1 1 0 1.3.2 2.5.6 3.6.1.3 0 .7-.2 1z"/></svg></span>
      <h4>Phone</h4>
      <p class="phone">206.555.0148</p>
    </div>
    <div class="footer-col">
      <span class="badge"><svg width="24" height="24" viewBox="0 0 24 24"><rect x="3" y="6" width="18" height="12" fill="none" stroke="#fff" stroke-width="2"/><path d="M3 6l9 7 9-7" fill="none" stroke="#fff" stroke-width="2"/></svg></span>
      <h4>Email</h4>
      <p>contact@pvtlawgroup.com</p>
      <div class="social"><i></i><i></i><i></i><i></i></div>
    </div>
  </div>
  <nav class="footer-nav">
    <span class="active">HOME</span><span>/</span><span>EXPERIENCE</span><span>/</span><span>ABOUT</span><span>/</span><span>CONTACT</span>
  </nav>
  <p class="copyright">©2008-2010 PVT LAW GROUP PLLC &nbsp;|&nbsp; All Rights Reserved.</p>
</footer>

</body>
</html>
```